Mental Health care Company in Washington DC

We are a new mental health care services provider in Washington DC. Please look at these sites.
https://marlowbrookpartners.com
https://www.quillstoneinc.com
https://velmarsh-kt.org/
https://www.trivanqx.com
https://www.thelanternofqz.com

```html
<!DOCTYPE html>
<html lang="en">
<head>
<meta charset="utf-8">
<title>Novari Health Services</title>
<link href="https://fonts.googleapis.com/css2?family=Lexend:wght@300;400;500;600&family=IBM+Plex+Sans:ital,wght@0,400;0,500;0,600;1,400&display=swap" rel="stylesheet">
<style>
:root{
  --navy:#0f2649;
  --navy-deep:#0b1f3e;
  --orange:#f4a465;
  --teal:#9fd8da;
  --ink:#1b2b45;
  --muted:#5a6272;
  --label:#9aa1ad;
  --soft:#f4f4f4;
  --footer:#1d1d1d;
  --white:#ffffff;
  --on-navy:#e4e8ef;
}
*{box-sizing:border-box;margin:0;padding:0}
html,body{width:1200px;height:4914px;overflow:hidden}
body{position:relative;background:var(--white);font-family:"IBM Plex Sans",sans-serif;color:var(--ink)}
.abs{position:absolute}
.heading{font-family:"Lexend",sans-serif;font-weight:500;color:var(--navy);letter-spacing:-.3px}
.label{font-family:"Lexend",sans-serif;font-size:11px;letter-spacing:3.5px;color:var(--label);text-transform:uppercase;display:flex;align-items:center;gap:8px}
.label .rule{width:32px;height:1.5px;background:var(--label)}
.btn{display:flex;align-items:center;justify-content:center;background:var(--orange);color:var(--navy);font-weight:600;font-size:13px;border-radius:20px}
.copy{font-size:13.5px;line-height:22px;color:var(--muted)}
.copy-on-navy{font-size:14px;line-height:26px;color:var(--on-navy)}

/* small section ornament: two dots */
.ornament{display:flex;gap:6px;width:34px}
.ornament span{width:12px;height:12px;border-radius:50%}
.ornament .o1{background:var(--orange)}
.ornament .o2{background:var(--teal)}
.ornament.center{justify-content:center}

/* header */
.brand{font-family:"Lexend",sans-serif;font-size:30px;font-weight:400;color:var(--navy);letter-spacing:-.5px}
.brand-sub{font-family:"Lexend",sans-serif;font-size:10px;letter-spacing:6px;color:var(--label)}
.nav{display:flex;gap:22px;font-size:13px;color:#4a5263}
.nav .active{color:var(--orange);font-weight:600}

/* hero */
.hero{left:0;top:84px;width:1200px;height:578px;border-radius:0 0 90px 90px;overflow:hidden;
  background:linear-gradient(90deg,rgba(20,40,80,.82) 0%,rgba(40,60,100,.45) 55%,rgba(120,130,150,.2) 100%),linear-gradient(120deg,#9b8e87,#6c6e7a 60%,#4a5060)}
.hero-kicker{font-family:"Lexend",sans-serif;font-size:20px;letter-spacing:4px;color:#fff;font-weight:300}
.hero-title{font-family:"Lexend",sans-serif;font-size:50px;line-height:58px;color:#fff;font-weight:600}
.hero-title .light{font-weight:300;color:var(--teal)}
.dot{width:12px;height:12px;border-radius:50%;border:1.5px solid rgba(255,255,255,.7)}
.dot.on{background:var(--orange);border-color:var(--orange)}

/* welcome */
.welcome{left:0;top:1509px;width:1200px;height:582px;background:var(--navy-deep)}
.why{left:0;top:2091px;width:1200px;height:317px;background:var(--soft)}
.card-over{background:linear-gradient(180deg,rgba(15,38,73,0) 45%,rgba(15,38,73,.92) 80%)}

/* testimonial */
.review{left:106px;top:3260px;width:992px;height:358px;background:var(--navy-deep);border-radius:4px;text-align:center;color:#fff}
.arrow{width:36px;height:36px;border-radius:50%;display:flex;align-items:center;justify-content:center}

/* footer */
.footer{left:0;top:4518px;width:1200px;height:396px;background:var(--footer);border-radius:90px 90px 0 0;color:#fff}
.ftitle{font-family:"Lexend",sans-serif;font-size:15px;font-weight:500}
.flinks{list-style:none;font-size:14px;line-height:32px}
.social{width:36px;height:36px;border-radius:50%;border:1px solid #bdbdbd}
.social.on{background:var(--teal);border-color:var(--teal)}
.ci{display:flex;gap:12px;font-size:13px;line-height:19px}
</style>
</head>
<body>

<!-- header -->
<div class="abs brand" style="left:104px;top:18px">Novari Health</div>
<div class="abs brand-sub" style="left:132px;top:55px">SERVICES</div>
<nav class="abs nav" style="left:315px;top:34px">
  <span class="active">Home</span><span>About Us</span><span>Therapies &amp; Treatment</span><span>Our Services</span><span>Gallery</span><span>Contact Us</span>
</nav>
<div class="abs btn" style="left:927px;top:23px;width:170px;height:39px;font-size:12px">Book An Appointment</div>

<!-- hero -->
<section class="abs hero" role="img" aria-label="Smiling family embracing beside a counsellor in glasses holding a clipboard"></section>
<div class="abs dot" style="left:43px;top:288px"></div>
<div class="abs dot on" style="left:43px;top:304px"></div>
<div class="abs dot" style="left:43px;top:320px"></div>
<div class="abs hero-kicker" style="left:106px;top:187px">Novari Health Services</div>
<h1 class="abs hero-title" style="left:104px;top:224px">Expert Care <span class="light">For Your</span><br><span class="light">Mental</span> Well-Being</h1>
<div class="abs" style="left:104px;top:354px;font-size:15px;color:#fff;font-weight:500">Compassionate Mental Health Support When You Need It Most</div>
<div class="abs btn" style="left:104px;top:395px;width:114px;height:37px">Get Started</div>

<!-- therapies -->
<div class="abs ornament" style="left:106px;top:764px"><span class="o1"></span><span class="o2"></span></div>
<h2 class="abs heading" style="left:104px;top:798px;font-size:42px">Therapies &amp; Treatment</h2>
<div class="abs label" style="left:105px;top:858px">Therapies &amp; Treatment <span class="rule"></span></div>
<p class="abs copy" style="left:624px;top:747px;width:472px">Lorem ipsum dolor sit amet, consectetur adipiscing elit, sed do eiusmod tempor incididunt ut labore et dolore magna aliqua. Ut enim ad minim veniam, quis nostrud exercitation ullamco laboris nisi ut aliquip ex ea commodo consequat.</p>
<div class="abs btn" style="left:624px;top:850px;width:107px;height:38px">Read More</div>
<div class="abs" style="left:104px;top:937px;width:993px;height:481px;background:linear-gradient(120deg,#d8d6d2,#b4aea6 50%,#e6e3de)" role="img" aria-label="Therapist and client talking in a bright office"></div>

<!-- welcome -->
<section class="abs welcome"></section>
<div class="abs" style="left:0;top:1509px;width:600px;height:582px;background:linear-gradient(135deg,#13294b,#1c3560 60%,#0f2244)" role="img" aria-label="Faint background of clasped hands in dark blue tones"></div>
<div class="abs ornament" style="left:643px;top:1578px"><span class="o1"></span><span class="o2"></span></div>
<h2 class="abs heading" style="left:642px;top:1608px;font-size:42px;line-height:52px;color:#fff">Welcome To<br>Novari Health Services</h2>
<div class="abs label" style="left:642px;top:1728px;color:#c9ced8">Who We Are <span class="rule" style="background:#c9ced8"></span></div>
<p class="abs copy-on-navy" style="left:642px;top:1773px;width:450px">Lorem ipsum dolor sit amet, consectetur adipiscing elit, sed do eiusmod tempor incididunt ut labore et dolore magna aliqua. Ut enim ad minim veniam, quis nostrud exercitation ullamco laboris nisi ut aliquip ex ea commodo consequat. Duis aute irure dolor in reprehenderit in voluptate velit esse cillum dolore eu fugiat nulla pariatur. Excepteur sint occaecat cupidatat non proident, sunt in culpa qui officia deserunt mollit anim id est laborum.</p>
<div class="abs btn" style="left:642px;top:1975px;width:106px;height:37px">Read More</div>

<!-- why choose -->
<section class="abs why"></section>
<div class="abs ornament" style="left:108px;top:2188px"><span class="o1"></span><span class="o2"></span></div>
<h2 class="abs heading" style="left:106px;top:2218px;font-size:42px;line-height:52px">Why Choose<br>Novari Health Services</h2>
<div class="abs label" style="left:106px;top:2333px">Therapies &amp; Treatment <span class="rule"></span></div>
<p class="abs copy" style="left:617px;top:2182px;width:472px">Lorem ipsum dolor sit amet, consectetur adipiscing elit, sed do eiusmod tempor incididunt ut labore et dolore magna aliqua. Ut enim ad minim veniam, quis nostrud exercitation ullamco laboris nisi ut aliquip ex ea commodo consequat.</p>
<div class="abs btn" style="left:617px;top:2285px;width:107px;height:38px">Read More</div>

<!-- services -->
<div class="abs ornament center" style="left:583px;top:2508px"><span class="o1"></span><span class="o2"></span></div>
<h2 class="abs heading" style="left:0;width:1200px;text-align:center;top:2540px;font-size:42px">Services We Offer</h2>
<div class="abs label" style="left:0;width:1200px;justify-content:center;top:2600px"><span class="rule"></span>How We Help You<span class="rule"></span></div>
<div class="abs" style="left:0;top:2684px;width:253px;height:302px;background:linear-gradient(135deg,#d9d3cb,#9f8c7e)" role="img" aria-label="Young woman speaking with a counsellor"></div>
<div class="abs" style="left:260px;top:2663px;width:435px;height:347px;background:linear-gradient(135deg,#cfc9c1,#8f8276)" role="img" aria-label="Couple in a family counselling session"></div>
<div class="abs card-over" style="left:260px;top:2663px;width:435px;height:347px"></div>
<div class="abs" style="left:260px;top:2937px;width:435px;text-align:center;color:#fff;font-size:16px;font-weight:500">Family Counseling &amp;Therapy</div>
<svg class="abs" style="left:468px;top:2966px" width="20" height="16" viewBox="0 0 20 16"><path d="M2 8h15M11 2l6 6-6 6" fill="none" stroke="#fff" stroke-width="2"/></svg>
<div class="abs" style="left:703px;top:2684px;width:251px;height:302px;background:linear-gradient(135deg,#d3d6d2,#7f8a86)" role="img" aria-label="Man in session while a counsellor takes notes"></div>
<div class="abs" style="left:961px;top:2684px;width:239px;height:302px;background:linear-gradient(135deg,#b9b3ab,#5e5a56)" role="img" aria-label="Distressed man talking with a therapist"></div>

<!-- testimonials -->
<div class="abs ornament center" style="left:583px;top:3112px"><span class="o1"></span><span class="o2"></span></div>
<h2 class="abs heading" style="left:0;width:1200px;text-align:center;top:3148px;font-size:42px">Client Testimonials</h2>
<div class="abs label" style="left:0;width:1200px;justify-content:center;top:3205px"><span class="rule"></span>Our Reviews<span class="rule"></span></div>
<div class="abs review">
  <div style="width:66px;height:66px;border-radius:50%;background:#c7ccd4;border:3px solid #fff;margin:48px auto 0" role="img" aria-label="Client portrait"></div>
  <div style="margin-top:18px;font-weight:600;font-size:15px">DALEN MARSH</div>
  <div style="color:#f6c23a;font-size:17px;letter-spacing:1px;line-height:20px">★★★★★</div>
  <p style="margin:20px auto 0;width:830px;font-style:italic;font-size:14.5px;line-height:27px">"Lorem ipsum dolor sit amet, consectetur adipiscing elit, sed do eiusmod tempor incididunt ut labore et dolore magna aliqua. Ut enim ad minim veniam, quis nostrud exercitation ullamco laboris nisi ut aliquip ex ea commodo consequat. Duis aute irure dolor in reprehenderit in voluptate velit esse cillum dolore eu fugiat nulla pariatur. Excepteur sint occaecat cupidatat non proident, sunt in culpa qui officia deserunt mollit anim id est laborum...</p>
</div>
<div class="abs arrow" style="left:40px;top:3425px;background:#111"><svg width="12" height="12" viewBox="0 0 12 12"><path d="M8 1L3 6l5 5" fill="none" stroke="#fff" stroke-width="2"/></svg></div>
<div class="abs arrow" style="left:1125px;top:3425px;background:#1d4fa0"><svg width="12" height="12" viewBox="0 0 12 12"><path d="M4 1l5 5-5 5" fill="none" stroke="#fff" stroke-width="2"/></svg></div>

<!-- portfolio -->
<div class="abs ornament center" style="left:583px;top:3718px"><span class="o1"></span><span class="o2"></span></div>
<h2 class="abs heading" style="left:0;width:1200px;text-align:center;top:3754px;font-size:42px">Our Portfolio</h2>
<div class="abs label" style="left:0;width:1200px;justify-content:center;top:3811px"><span class="rule"></span>Our Gallery<span class="rule"></span></div>
<div class="abs" style="left:0;top:3878px;width:507px;height:268px;background:linear-gradient(135deg,#d8d2c8,#8c8074)" role="img" aria-label="Counsellor with clipboard listening to a client"></div>
<div class="abs" style="left:519px;top:3878px;width:335px;height:268px;background:linear-gradient(135deg,#cfd2cf,#6b7686)" role="img" aria-label="Two women talking in a session"></div>
<div class="abs" style="left:866px;top:3878px;width:334px;height:268px;background:linear-gradient(135deg,#d6d3cc,#8a7a5c)" role="img" aria-label="Group therapy circle"></div>
<div class="abs" style="left:0;top:4160px;width:333px;height:268px;background:linear-gradient(135deg,#dfe2e4,#8d8f96)" role="img" aria-label="Therapist writing notes during a session"></div>
<div class="abs" style="left:345px;top:4160px;width:336px;height:268px;background:linear-gradient(135deg,#e2ddd6,#8c7f76)" role="img" aria-label="Woman in distress with a counsellor"></div>
<div class="abs" style="left:692px;top:4160px;width:508px;height:268px;background:linear-gradient(135deg,#dfe3ea,#5e6b80)" role="img" aria-label="Older man speaking in a counselling room"></div>

<!-- footer -->
<footer class="abs footer">
  <div class="abs brand" style="left:104px;top:90px;color:#fff;font-size:40px">Novari Health</div>
  <div class="abs brand-sub" style="left:148px;top:142px;color:#fff;font-size:13px;letter-spacing:8px">SERVICES</div>
  <div class="abs social on" style="left:132px;top:176px"></div>
  <div class="abs social" style="left:182px;top:176px"></div>
  <div class="abs social" style="left:229px;top:176px"></div>

  <div class="abs ftitle" style="left:397px;top:64px">QUICK LINKS</div>
  <ul class="abs flinks" style="left:397px;top:120px">
    <li>Home</li><li>About Us</li><li>Therapies &amp; Treatment</li><li>Our Services</li><li>Gallery</li><li>Contact Us</li>
  </ul>
  <div class="abs" style="left:597px;top:64px;width:1px;height:240px;background:#777"></div>

  <div class="abs ftitle" style="left:620px;top:64px">CONTACT US</div>
  <div class="abs ci" style="left:628px;top:130px">
    <svg width="14" height="14" viewBox="0 0 24 24"><path fill="#fff" d="M6.6 10.8a15 15 0 006.6 6.6l2.2-2.2c.3-.3.7-.4 1-.2 1.1.4 2.3.6 3.6.6.6 0 1 .4 1 1V20c0 .6-.4 1-1 1A17 17 0 013 4c0-.6.4-1 1-1h3.5c.6 0 1 .4 1 1 0 1.3.2 2.5.6 3.6.1.3 0 .7-.2 1z"/></svg>
    <div>PHONE NO:<br>+1(555) 014 2290</div>
  </div>
  <div class="abs ci" style="left:628px;top:192px">
    <svg width="16" height="14" viewBox="0 0 24 20"><path fill="#fff" d="M2 2h20v16H2zm2 2v1l8 5 8-5V4z"/></svg>
    <div>EMAIL:<br>info@novarihealth.com</div>
  </div>
  <div class="abs ci" style="left:628px;top:256px">
    <svg width="14" height="18" viewBox="0 0 24 30"><path fill="#fff" d="M12 0a10 10 0 00-10 10c0 8 10 20 10 20s10-12 10-20A10 10 0 0012 0zm0 14a4 4 0 110-8 4 4 0 010 8z"/></svg>
    <div>LOCATION:<br>Lorem ipsum dolor sit<br>consectetur.</div>
  </div>
  <div class="abs" style="left:835px;top:64px;width:1px;height:240px;background:#777"></div>

  <div class="abs ftitle" style="left:866px;top:64px">OUR NEWSLETTER</div>
  <div class="abs" style="left:862px;top:130px;width:232px;height:38px;background:#fff;border-radius:6px;font-size:9px;color:#999;padding:13px 10px">Email Address</div>
  <div class="abs btn" style="left:862px;top:186px;width:107px;height:38px">Subscribe</div>

  <div class="abs" style="left:104px;top:337px;width:993px;height:1px;background:#666"></div>
  <div class="abs" style="left:0;width:1200px;text-align:center;top:356px;font-size:13px">Copyright © 2025 <span style="color:var(--teal);text-decoration:underline">Novari Health Services</span> | All Rights Reserved.</div>
</footer>

</body>
</html>
```